Kestavon Values/Culture for employees

Take our cultures list and create an on brand graphic that can be used for various media, ie. posters, screen savers etc. mykestavon.com
We're a medium sized company who installs permanent christmas lights primarily for homeowners. however we will do it for businesses as well. This graphic is going to be for our employees to help remind them the cultures and values we stand for to provide the best experience and products. Since Christmas lights are such an important part of our country's culture we want to make sure the internal culture of the company reflects that.

Target Market(s)

People who want to imrpove their home with permanent chrismas lights and never install them again

Requirements
Must have
• Proper styling with our brand colors and font (gotham)

Style guide is attached.

```html
<!DOCTYPE html>
<html lang="en">
<head>
<meta charset="utf-8">
<title>Kestavon – Our Cultural Beliefs</title>
<link href="https://fonts.googleapis.com/css2?family=Montserrat:wght@500;600;700;800&display=swap" rel="stylesheet">
<style>
  :root {
    --green: #7fba3a;
    --red: #fe0000;
    --orange: #ff8a2e;
    --blue: #1f6bff;
    --teal: #32cc96;
    --pink: #ff3399;
    --black: #000;
    --white: #fff;
  }
  * { box-sizing: border-box; margin: 0; padding: 0; }
  html, body { width: 1200px; height: 927px; overflow: hidden; background: var(--white); }
  body { font-family: "Montserrat", Arial, sans-serif; color: var(--white); position: relative; }

  .stripes { position: absolute; left: 0; width: 1200px; display: grid; grid-template-columns: repeat(6, 200px); }
  .stripes.top { top: 0; height: 102px; }
  .green { background: var(--green); }
  .red { background: var(--red); }
  .orange { background: var(--orange); }
  .blue { background: var(--blue); }
  .teal { background: var(--teal); }
  .pink { background: var(--pink); }

  .banner { position: absolute; top: 108px; left: 0; width: 1200px; height: 137px; background: var(--black); overflow: hidden; }
  .banner .bokeh { position: absolute; left: 0; top: 0; width: 520px; height: 137px;
    background: radial-gradient(circle at 10% 60%, rgba(255,90,200,.55), transparent 35%),
                radial-gradient(circle at 30% 20%, rgba(80,140,255,.45), transparent 30%),
                radial-gradient(circle at 45% 80%, rgba(255,150,60,.35), transparent 30%),
                linear-gradient(90deg, #2a1a3a, #000 100%); }
  .banner .house { position: absolute; right: 0; top: 0; width: 120px; height: 137px;
    background: linear-gradient(160deg, #5b6fd6 0%, #2b2f7a 45%, #140f2e 100%); }
  .banner h1 { position: absolute; left: 52px; top: 134px; transform: translateY(-100%); top: 208px;
    font-size: 71px; font-weight: 800; letter-spacing: 0.5px; line-height: 1; }
  .banner .brand { position: absolute; left: 845px; top: 204px; top: 96px; font-size: 22px; font-weight: 600;
    letter-spacing: 8px; }

  .values { position: absolute; top: 251px; left: 0; width: 1200px; height: 594px; display: grid; grid-template-columns: repeat(6, 200px); }
  .value { position: relative; padding: 0 10px 0 24px; }
  .value .icon { position: absolute; left: 50%; top: 76px; width: 90px; height: 120px; transform: translateX(-50%); }
  .value .icon svg { width: 100%; height: 100%; fill: none; stroke: var(--white); stroke-width: 4; stroke-linecap: round; stroke-linejoin: round; }
  .value h2 { position: absolute; left: 0; right: 0; top: 218px; text-align: center; font-size: 21.5px; font-weight: 600; letter-spacing: 0; white-space: nowrap; }
  .value p { position: absolute; left: 24px; right: 6px; top: 286px; font-size: 18.5px; font-weight: 700; line-height: 30.6px; }

  .rainbow { position: absolute; top: 849px; left: 0; width: 1200px; height: 14px;
    background: linear-gradient(90deg, #6a7fb8 0%, #b43a8a 20%, #e8364f 45%, #f47a3a 60%, #f7c040 75%, #7fc6a6 100%); }
  .footer { position: absolute; top: 868px; left: 0; width: 1200px; height: 59px; background: var(--black); overflow: hidden; }
  .footer .bokeh { position: absolute; inset: 0;
    background: radial-gradient(circle at 5% 50%, rgba(120,160,255,.4), transparent 18%),
                radial-gradient(circle at 92% 40%, rgba(220,190,80,.35), transparent 15%),
                radial-gradient(circle at 75% 70%, rgba(255,80,120,.3), transparent 12%); }
  .footer .url { position: absolute; left: 0; right: 0; top: 19px; text-align: center; font-size: 15.5px; font-weight: 700; }
  .footer .url svg { width: 14px; height: 14px; vertical-align: -2px; margin-right: 6px; fill: none; stroke: var(--white); stroke-width: 1.4; }
</style>
</head>
<body>
  <div class="stripes top">
    <div class="green"></div><div class="red"></div><div class="orange"></div>
    <div class="blue"></div><div class="teal"></div><div class="pink"></div>
  </div>

  <header class="banner">
    <div class="bokeh" role="img" aria-label="Blurred colourful holiday lights"></div>
    <div class="house" role="img" aria-label="Home lit with permanent colourful roofline lights at dusk"></div>
    <h1 style="top:46px;transform:none;">Our Cultural Beliefs</h1>
    <div class="brand">KESTAVON</div>
  </header>

  <main class="values">
    <section class="value green">
      <div class="icon"><svg viewBox="0 0 90 120"><circle cx="45" cy="27" r="20"/><path d="M6 112 V78 Q6 48 45 48 Q84 48 84 78 V112 L66 108 M6 112 L28 108"/><path d="M36 72 L42 66 V108 M34 108 H52"/></svg></div>
      <h2>CUSTOMER FIRST</h2>
      <p>I strive to meet our customer’s needs and deliver exceptional experiences. others.</p>
    </section>
    <section class="value red">
      <div class="icon"><svg viewBox="0 0 90 120"><path d="M6 20 L45 62 L84 20"/><path d="M6 40 L45 82 L84 40"/></svg></div>
      <h2>OWN IT</h2>
      <p>I demonstrate commitment by showing up “all in,” all the time, even when it requires sacrifice.</p>
    </section>
    <section class="value orange">
      <div class="icon" style="width:120px"><svg viewBox="0 0 120 120"><path d="M4 64 A46 46 0 0 1 92 50"/><circle cx="52" cy="66" r="34"/><circle cx="48" cy="58" r="20"/><path d="M28 58 H112 M98 44 L112 58 L98 72"/></svg></div>
      <h2>SIMPLIFY</h2>
      <p>I eliminate complexity and solve problems for sustainable results.</p>
    </section>
    <section class="value blue">
      <div class="icon" style="width:160px"><svg viewBox="0 0 160 120"><path d="M4 60 L28 74 L50 36 L30 22"/><path d="M156 60 L132 74 L110 36 L130 22"/><path d="M50 36 Q66 28 90 34 L62 48 Q56 56 66 58 L96 44 L128 74"/><path d="M36 72 L70 104 Q78 110 84 102 L104 86 L122 78"/><path d="M48 74 L62 88 M58 66 L74 84 M70 62 L86 78"/></svg></div>
      <h2>BUILD TRUST</h2>
      <p>I trust people to do their best, let them perform and then coach them to perform at even higher levels.</p>
    </section>
    <section class="value teal">
      <div class="icon" style="width:120px"><svg viewBox="0 0 120 120"><circle cx="60" cy="60" r="28"/><path d="M60 40 L65 55 L80 60 L65 65 L60 80 L55 65 L40 60 L55 55 Z"/><path d="M60 4 V20 M60 100 V116 M4 60 H20 M100 60 H116 M20 20 L32 32 M88 88 L100 100 M100 20 L88 32 M32 88 L20 100"/></svg></div>
      <h2>SEIZE THE DAY</h2>
      <p>I am a big part of something big. What I do today will help us win together!</p>
    </section>
    <section class="value pink">
      <div class="icon"><svg viewBox="0 0 90 120"><path d="M28 114 V90 Q8 76 8 50 V38 Q8 30 18 30 L30 30 V16 Q30 8 40 8 Q50 8 50 16 V30 M50 22 Q50 14 58 14 Q66 14 66 22 V34 Q72 28 78 34 Q84 40 82 60 Q80 82 72 90 V114"/><path d="M30 30 V48 M50 30 V46 M66 34 V48 M30 48 Q20 56 28 64 M28 90 Q46 96 60 90"/></svg></div>
      <h2>DO IT NOW</h2>
      <p>I work above the line, continue to ask “What else can I do to deliver results?” and refuse to blame others.</p>
    </section>
  </main>

  <div class="rainbow"></div>

  <footer class="footer">
    <div class="bokeh" role="img" aria-label="Blurred colourful holiday lights"></div>
    <div class="url"><svg viewBox="0 0 14 14"><circle cx="7" cy="7" r="6"/><ellipse cx="7" cy="7" rx="2.6" ry="6"/><path d="M1 7 H13 M2 4 H12 M2 10 H12"/></svg>www.mykestavon.com</div>
  </footer>
</body>
</html>
```